Banner 34"x81"

This is for a Pull Up Banner
I am supplying a sample of my logo and some of my art work for you to incorporate into an upright banner.
Please business name:LuellaRo OpenHarbor Psychotherapy
phone number: 583-214-9067 NOT THE ONE ON THE BUSINESS CARD

```html
<!DOCTYPE html>
<html lang="en">
<head>
<meta charset="utf-8">
<title>LuellaRo OpenHarbor Psychotherapy – Pull Up Banner</title>
<link rel="stylesheet" href="https://fonts.googleapis.com/css2?family=Rubik:wght@400;700&family=Montserrat:wght@500;600&display=swap">
<style>
  :root {
    --backdrop: #d4d5d9;
    --paper: #ffffff;
    --wave-blue: #4a5c9a;
    --navy: #1e3464;
    --contact-ink: #3f4f8f;
    --mark-blue: #2a5bb0;
    --portrait-dark: #3a2a27;
    --portrait-blue: #2f5fc0;
  }
  * { margin: 0; padding: 0; box-sizing: border-box; }
  html, body {
    width: 1200px; height: 4131px; overflow: hidden;
    background: var(--backdrop);
  }
  .banner {
    position: absolute; left: 50px; top: 755px;
    width: 1100px; height: 2620px;
    background: var(--paper);
    overflow: hidden;
    box-shadow: 0 10px 40px rgba(0,0,0,0.18);
  }
  .banner__shapes { position: absolute; inset: 0; }
  .wave { fill: var(--wave-blue); }

  .masthead {
    position: absolute; left: 0; right: 0; top: 60px;
    text-align: center; color: var(--navy);
    font-family: "Rubik", Arial, sans-serif;
  }
  .masthead__tagline { font-size: 70px; font-weight: 400; line-height: 1; letter-spacing: -0.5px; }
  .masthead__name { font-size: 168px; font-weight: 700; line-height: 1; margin-top: 14px; letter-spacing: -1px; }
  .masthead__service { font-size: 80px; font-weight: 400; line-height: 1; margin-top: 10px; }

  .portrait {
    position: absolute; left: -18px; top: 679px;
    width: 972px; height: 972px; border-radius: 50%;
    border: 16px solid var(--paper);
    background: radial-gradient(circle at 52% 45%, #6b4a3e 0%, var(--portrait-dark) 45%, #22181a 70%),
                var(--portrait-dark);
    overflow: hidden;
  }
  .portrait::after {
    content: ""; position: absolute; left: 18%; right: 12%; bottom: 0; height: 42%;
    background: linear-gradient(180deg, #3b6ad0, var(--portrait-blue));
    border-radius: 40% 40% 0 0;
  }

  .contacts {
    position: absolute; left: 112px; top: 1745px;
    list-style: none;
    font-family: "Montserrat", Arial, sans-serif;
    font-weight: 600; font-size: 41px; color: var(--contact-ink);
  }
  .contacts__item { display: flex; align-items: center; height: 92px; }
  .contacts__icon { width: 46px; height: 46px; margin-right: 28px; flex: none; }

  .brand-mark {
    position: absolute; left: 669px; top: 2190px;
    display: flex; align-items: center; gap: 22px;
    font-family: "Rubik", Arial, sans-serif;
    font-weight: 700; font-size: 150px; line-height: 1; color: var(--navy);
  }
  .brand-mark__square { width: 46px; height: 46px; background: var(--mark-blue); }
</style>
</head>
<body>
  <main class="banner">
    <svg class="banner__shapes" viewBox="0 0 1100 2620" width="1100" height="2620" aria-hidden="true">
      <path class="wave wave--upper" d="M0,545 C60,600 150,640 260,620 C370,600 520,505 700,520 C860,535 980,655 1100,664 L1100,1605 C1000,1680 900,1710 780,1712 L468,1660 L0,1165 Z"/>
      <path class="wave wave--lower" d="M0,2480 C100,2432 250,2420 400,2468 C500,2505 565,2560 680,2556 C800,2552 880,2490 960,2442 C1020,2410 1070,2418 1100,2440 L1100,2620 L0,2620 Z"/>
    </svg>

    <header class="masthead">
      <p class="masthead__tagline">OpenHarbor</p>
      <h1 class="masthead__name">LuellaRo</h1>
      <p class="masthead__service">Psychotherapy</p>
    </header>

    <div class="portrait" role="img" aria-label="Portrait photo of the therapist seated in a dark leather chair, wearing a blue top"></div>

    <ul class="contacts">
      <li class="contacts__item">
        <svg class="contacts__icon" viewBox="0 0 46 46" aria-hidden="true">
          <circle cx="23" cy="23" r="23" fill="var(--contact-ink)"/>
          <path d="M15 12 l5 0 l2 7 l-3 2 c1.5 3 3.5 5 6 6 l2 -3 l7 2 l0 5 c-11 1 -20 -8 -19 -19 z" fill="#fff"/>
        </svg>
        <span>583-214-9067</span>
      </li>
      <li class="contacts__item">
        <svg class="contacts__icon" viewBox="0 0 46 46" aria-hidden="true"><circle cx="23" cy="23" r="23" fill="var(--contact-ink)"/></svg>
        <span>@LuellaHarbor</span>
      </li>
      <li class="contacts__item">
        <svg class="contacts__icon" viewBox="0 0 46 46" aria-hidden="true"><circle cx="23" cy="23" r="23" fill="var(--contact-ink)"/></svg>
        <span>@LuellaOpenHarbor</span>
      </li>
      <li class="contacts__item">
        <svg class="contacts__icon" viewBox="0 0 46 46" aria-hidden="true">
          <circle cx="23" cy="23" r="23" fill="var(--contact-ink)"/>
          <rect x="12" y="15" width="22" height="16" rx="2" fill="#fff"/>
          <path d="M12 16 l11 8 l11 -8" fill="none" stroke="var(--contact-ink)" stroke-width="2"/>
        </svg>
        <span>LuellaOpenHarbor@mailbox.com</span>
      </li>
    </ul>

    <div class="brand-mark">
      <span class="brand-mark__square" aria-hidden="true"></span>
      <span class="brand-mark__name">LR</span>
    </div>
  </main>
</body>
</html>
```